Intermodal Trucking Company Website

My client is a trucking company that takes the containers you see on the back of a ship or railroad car and delivers them in the midwestern part of the United States. Here are some of their competitors Websites and their logo to use as part of the design.

http://www.varnekhaulers.example/
https://www.plirext.example/
http://www.brontagefreight.example/
https://www.lqp-xy.example/

Industry/Entity Type

Trucking Company

Number of Pages Required

2 page

Requirements
Must have
• Website must be professional and the design needs to be suitable for a responsive Website.
Should not have
• Please do not submit designs with misspellings. Designs with misspellings will be eliminated.

```html
<!DOCTYPE html>
<html lang="en">
<head>
<meta charset="utf-8">
<title>Tandem Rail Inc. – Transport &amp; Logistics</title>
<link rel="stylesheet" href="https://fonts.googleapis.com/css2?family=Roboto:wght@400;500;700&family=Roboto+Condensed:wght@700&display=swap">
<style>
:root{
  --white:#ffffff;
  --black:#000000;
  --ink:#333333;
  --orange:#f39c1f;
  --orange-deep:#ee9a26;
  --red:#a80000;
  --red-dark:#a50000;
  --red-title:#b00d0d;
  --field:#ecdada;
  --field-border:#c94a3c;
  --frame:#b9b2a8;
}
*{box-sizing:border-box;margin:0;padding:0}
html,body{width:1200px;height:950px;overflow:hidden;background:var(--white);font-family:"Roboto",Arial,sans-serif}
.page{position:relative;width:1200px;height:950px}

/* header */
.site-header{position:absolute;top:0;left:0;width:1200px;height:104px;background:var(--white)}
.brand{position:absolute;left:86px;top:34px;display:flex;align-items:center;gap:8px;font-weight:700;font-size:17px;color:var(--red)}
.brand-mark{width:14px;height:14px;background:var(--red)}
.contact{position:absolute;top:36px;display:flex;gap:8px;color:var(--ink)}
.contact svg{flex:none;margin-top:2px}
.contact-main{font-size:14px;line-height:17px}
.contact-sub{font-size:12px;line-height:16px}
.contact-phone{left:487px}
.contact-address{left:847px}

/* nav */
.main-nav{position:absolute;top:104px;left:0;width:1200px;height:53px;background:var(--black)}
.nav-links{position:absolute;left:99px;top:0;display:flex;gap:17px;list-style:none}
.nav-links li{position:relative;height:53px;line-height:54px;color:var(--white);font-weight:700;font-size:16.7px}
.nav-links li.active::after{content:"";position:absolute;left:0;right:0;bottom:0;height:4px;background:var(--orange)}
.track-form{position:absolute;left:880px;top:113px;width:237px;height:34px;display:flex;border-radius:17px;overflow:hidden;border:1px solid var(--orange)}
.track-input{flex:1;background:var(--field);color:#666;font-size:16.5px;line-height:32px;padding-left:22px}
.track-button{width:68px;background:var(--orange);color:var(--white);font-weight:700;font-size:16.5px;line-height:32px;text-align:center}

/* hero */
.hero{position:absolute;top:157px;left:0;width:1200px;height:510px}
.hero-photo{position:absolute;inset:0;background:linear-gradient(180deg,#6a676b 0%,#7e7470 40%,#574a45 65%,#2e2b2d 100%)}
.hero-eyebrow{position:absolute;left:98px;top:114px;color:var(--orange);font-weight:700;font-size:27px;text-shadow:0 2px 3px rgba(0,0,0,.4)}
.hero-title{position:absolute;left:97px;top:183px;color:var(--white);font-weight:700;font-size:43.5px;letter-spacing:.3px;text-shadow:0 2px 4px rgba(0,0,0,.5)}
.hero-sub{position:absolute;left:99px;top:238px;color:var(--white);font-weight:500;font-size:28.6px;text-shadow:0 2px 4px rgba(0,0,0,.5)}

.quote-panel{position:absolute;left:815px;top:50px;width:304px;height:411px;background:var(--orange-deep);border:4px solid var(--frame);border-radius:7px;padding:17px 18px 0 17px}
.quote-title{font-family:"Roboto Condensed",Arial,sans-serif;font-weight:700;font-size:32px;color:var(--red-title);letter-spacing:-.6px;margin-left:0;line-height:36px;white-space:nowrap}
.quote-fields{margin-top:13px;display:flex;flex-direction:column;gap:13px}
.quote-field{height:40px;background:var(--field);border:1px solid var(--field-border);font-size:17px;line-height:38px;color:#555;padding-left:10px}
.quote-submit{height:40px;background:var(--red-dark);color:var(--white);font-weight:700;font-size:17px;line-height:40px;text-align:center}

/* about */
.about{position:absolute;top:667px;left:0;width:1200px;height:283px;background:var(--red)}
.about-text{position:absolute;left:100px;top:22px;width:505px;color:var(--white);font-size:18.5px;line-height:22.7px;text-align:justify;letter-spacing:.2px}
.about-text p+p{margin-top:22px}
.about-text p.last{text-align:left}
.signature{position:absolute;left:100px;top:203px;color:var(--white)}
.signature-name{font-weight:700;font-size:19px;line-height:22px}
.signature-role{font-size:16.5px;line-height:20px}
.about-video{position:absolute;left:711px;top:27px;width:405px;height:227px;background:linear-gradient(180deg,#dcdcdc 0%,#c6c4c8 55%,#8c8598 100%)}
.play-button{position:absolute;left:180px;top:91px}
</style>
</head>
<body>
<div class="page">
  <header class="site-header">
    <div class="brand"><span class="brand-mark"></span>Tandem Rail Inc.</div>
    <div class="contact contact-phone">
      <svg width="28" height="28" viewBox="0 0 24 24" fill="none" stroke="#c0282d" stroke-width="1.6" stroke-linejoin="round"><path d="M5 3h4l2 5-2.5 1.5a11 11 0 0 0 6 6L16 13l5 2v4a2 2 0 0 1-2 2A17 17 0 0 1 3 5a2 2 0 0 1 2-2z"/><path d="M14 3a7 7 0 0 1 7 7M14 6.5a3.5 3.5 0 0 1 3.5 3.5"/></svg>
      <div><div class="contact-main">913-555-0142</div><div class="contact-sub">enquire@tandemrail.example</div></div>
    </div>
    <div class="contact contact-address">
      <svg width="24" height="30" viewBox="0 0 20 26" fill="none" stroke="#c0282d" stroke-width="1.5"><path d="M10 25s8-8.5 8-15A8 8 0 0 0 2 10c0 6.5 8 15 8 15z"/><circle cx="10" cy="10" r="3"/></svg>
      <div><div class="contact-main">418 West Ridge Avenue</div><div class="contact-sub">Kansas City, KS 66110</div></div>
    </div>
  </header>

  <nav class="main-nav">
    <ul class="nav-links">
      <li class="active">HOME</li><li>COMPANY</li><li>SERVICES</li><li>NEWS</li><li>CONTACT</li>
    </ul>
  </nav>
  <div class="track-form"><div class="track-input">Enter Tracking ID</div><div class="track-button">Track</div></div>

  <section class="hero">
    <div class="hero-photo" role="img" aria-label="Red semi truck hauling a container trailer on a highway at dusk"></div>
    <div class="hero-eyebrow">TANDEM RAIL INC.</div>
    <h1 class="hero-title">FAST - SECURED - RELIABLE</h1>
    <div class="hero-sub">Transport &amp; Logistics Service</div>

    <form class="quote-panel">
      <h2 class="quote-title">Request a Free Quote</h2>
      <div class="quote-fields">
        <div class="quote-field">Company / Contact Name</div>
        <div class="quote-field">Phone</div>
        <div class="quote-field">Email</div>
        <div class="quote-field">Origin</div>
        <div class="quote-field">Destination</div>
        <div class="quote-submit">Submit Information</div>
      </div>
    </form>
  </section>

  <section class="about">
    <div class="about-text">
      <p>Tandem Rail Inc. was established with the sole aim of enabling growth, by providing efficient and prompt logistics, freight forwarding &amp; transportation solutions for Export/Import bound cargo.</p>
      <p class="last">In addition, it also offers various other support services like warehousing, customs clearance and documentation, etc.</p>
    </div>
    <div class="signature">
      <div class="signature-name">Aren Malloy</div>
      <div class="signature-role">Founder &amp; President</div>
    </div>
    <div class="about-video" role="img" aria-label="Video still of the company founder seated at a desk with a laptop in a bright office">
      <svg class="play-button" width="44" height="44" viewBox="0 0 44 44"><circle cx="22" cy="22" r="20.5" fill="rgba(0,0,0,.15)" stroke="#fff" stroke-width="2"/><path d="M17 13l13 9-13 9z" fill="#fff"/></svg>
    </div>
  </section>
</div>
</body>
</html>
```